Meridian Harvest Partners- Web & Business card design for a new business within the Ag Sector

HELLO!!!!

We need your help in relation to web design (business cards and stationary if possible!) for a new company based in NSW, Australia.

The name of the business is: Meridian Harvest Partners (MHP). I have quickly mocked a webpage just to give you an idea of what we are looking for.... http://corvelland7.sitebuilderdemo.net/http

MHP is a strategic advisory, investment manager and problem solver within the Australian Agricultural sector.

Our Mission:

We are here to provide solutions to ALL of our Clients needs and desires within the Agricultural space.

Our Team:

Our team has worked with some of the largest & oldest Agricultural companies in Australia

We provide our Clients with a unique blend of the best Corporate as well as Operational experience that the Industry has to offer.

Client-driven Services Approach:

MHP offers a tailored service in order to meet the objectives and outcomes for each and every client.

Some of our services include:

- Food Security / Supply

- Procurement strategies within and across agricultural supply-chains

- Strategic Agribusiness advice for both Australian and Chinese based agricultural enterprises

- M&A / Due Diligence

- Corporate governance & risk management strategies.

I have attached a copy of our capability statement for background reading.

We look forward to receiving your designs!!!!!!!
Updates

Target Market(s)

Corporate, Family Offices, Food Services & Supermarkets - that are looking to obtain products within the agricultural space. Whether it be boxed beef, grain, live animals, advice - ie M&A, Due diligence - just think anything "Agricultural" and we can provide a solution

Industry/Entity Type

Agriculture

Contact Information for Business Card

See below

With respect to the business cards:

There are 2 Managing Directors:

1. Marcus Tilden
Managing Director
E: marcus.tilden@meridianharvestpartners.example
M: +61 400 913 642
W: www.meridianharvestpartners.example

2. Rachel Dunmore
Managing Director
E: rachel.dunmore@meridianharvestpartners.example
M: +61 400 276 418

Please see attached 2 * Files named Brenwick that outline a layout of business card that I like

Coding

Coded - Design and coding required

Number of Pages Required

5+ page

Font styles to use
Sans Serif
Other font styles liked:
• Calibri

Requirements
Must have
• I like the look of this website: http://fieldvoxtrend.example/
• And I like the themes in the website that I have mocked up: http://corvelland7.sitebuilderdemo.net/http
• The wow factor, with a professional twist.
• With respect to the website - would like it to follow the flow of the capability statement - ie with a home page, and the four additional pages:
• ABOUT US
• OUR SERVICES
• OUR TEAM
• CONTACT DETAILS
• The powerpoint presentation that I have attached is simply there for content direction - not design direction.
• As a result, am looking for web design / business card that stands out - is corporate - yet still agricultural feel.
• "capability statement" simply refers to a document that outlines our capabilities - and does not form part of the business name.
• A black angus cow, or a stalk of wheat - greens and yellows may better represent the Ag space.
• This s a draft mock-up of a web-site I created with one of those free web-page makers... This should give you a feel - crisp - whites - yet agricultural tones to highlight
• The attachments below should be used as inspiration - and don't need to be the actual shots used.

```html
<!DOCTYPE html>
<html lang="en">
<head>
<meta charset="utf-8">
<title>Meridian Harvest Partners</title>
<link href="https://fonts.googleapis.com/css2?family=Titillium+Web:ital,wght@0,300;0,400;0,600;0,700;1,400;1,600&display=swap" rel="stylesheet">
<style>
:root{
  --gold:#f5b400;
  --ink:#3a3a3a;
  --muted:#8a8a8a;
  --line:#e3e3e3;
  --green-deep:#1f5a10;
  --footer:#333333;
  --white:#ffffff;
}
*{box-sizing:border-box;margin:0;padding:0}
html,body{width:836px;height:1200px;overflow:hidden;background:var(--white)}
body{position:relative;font-family:"Titillium Web",Arial,sans-serif;color:var(--ink)}
.abs{position:absolute}

/* header */
.site-header{left:0;top:0;width:836px;height:73px;background:var(--white);border-bottom:4px solid var(--gold)}
.brand{left:130px;top:24px;font-size:15.5px;font-weight:400;color:var(--ink);letter-spacing:.2px;white-space:nowrap}
.nav{left:431px;top:31px;display:flex;gap:24px;font-size:8px;text-transform:uppercase;color:var(--ink);white-space:nowrap}
.nav .active{color:var(--gold)}

/* hero */
.hero{left:0;top:73px;width:836px;height:297px;
  background:linear-gradient(180deg,#7ed3cc 0%,#a9ddc4 35%,#c8d79a 52%,#c9a53a 62%,#c8961e 80%,#b7851a 100%)}
.hero-title{left:455px;top:44px;width:360px;text-align:left;font-size:30px;line-height:1.22;font-weight:700;color:#3b3b3b;text-transform:uppercase}
.hero-dots{left:680px;top:273px;display:flex;gap:3px}
.hero-dots span{width:5px;height:5px;border-radius:50%;background:var(--white)}

/* intro */
.intro{left:130px;top:392px;width:576px;text-align:center;font-style:italic;font-weight:600;font-size:14.5px;line-height:18px;color:var(--gold)}
.divider{left:150px;top:449px;width:536px;height:1px;background:var(--line)}

/* feature cards */
.card{top:471px;width:179px}
.card .photo{width:179px;height:98px}
.card h3{margin-top:11px;font-size:14px;font-weight:400;color:var(--ink)}
.card p{margin-top:3px;font-size:7.5px;line-height:13px;color:var(--muted)}

/* statement band */
.band{left:0;top:660px;width:836px;height:191px;background:linear-gradient(135deg,#2a6a14 0%,#1f5a10 50%,#2d6e16 100%)}
.band-text{left:0;top:42px;width:836px;text-align:center;color:var(--white);font-style:italic;font-size:18px;line-height:21px}
.band-text p+p{margin-top:22px}

/* services */
.video{left:130px;top:889px;width:259px;height:168px;background:linear-gradient(160deg,#7fc6ea 0%,#b8e0ef 30%,#e2c04a 55%,#c9951c 100%)}
.play{left:113px;top:72px;width:34px;height:24px}
.services{left:426px;top:885px;width:280px}
.services h2{font-size:14px;font-weight:400;color:var(--ink)}
.services .lead{margin-top:6px;font-size:7px;line-height:13px;color:var(--muted)}
.services ul{list-style:none;margin-top:14px}
.services li{position:relative;padding-left:12px;font-size:9.5px;line-height:13px;color:#555;margin-bottom:6px}
.services li::before{content:"";position:absolute;left:0;top:3px;width:7px;height:7px;border-radius:50%;border:1.5px solid var(--gold)}

/* footer */
.site-footer{left:0;top:1102px;width:836px;height:98px;background:var(--footer);color:var(--white)}
.f-title{font-size:12.5px;font-weight:600}
.signup{left:130px;top:17px}
.signup-form{left:130px;top:44px;display:flex;width:259px;height:29px}
.signup-form .field{flex:1;background:var(--white);font-size:7.5px;color:#666;padding:10px 6px}
.signup-form .btn{width:60px;background:var(--gold);font-size:8px;text-transform:uppercase;text-align:center;padding-top:10px}
.contact{left:427px;top:17px}
.contact .addr{margin-top:5px;font-size:7.5px;line-height:12px;color:#bbb}
.contact .phone{margin-top:3px;font-size:8px;color:var(--white)}
.social{left:598px;top:26px}
.copyright{left:576px;top:60px;font-size:7.5px;color:#bbb}
</style>
</head>
<body>

<header class="site-header abs">
  <div class="brand abs">MERIDIAN HARVEST PARTNERS (MHP)</div>
  <nav class="nav abs">
    <span class="active">Home</span><span>About Us</span><span>Our Services</span><span>Our Team</span><span>Contact</span>
  </nav>
</header>

<section class="hero abs" role="img" aria-label="Yellow combine harvester cutting a golden wheat field under a bright sky">
  <h1 class="hero-title abs">Meridian Harvest<br>Partners</h1>
  <div class="hero-dots abs"><span></span><span></span><span></span></div>
</section>

<p class="intro abs">MHP is a strategic advisory, investment manager and problem<br>solver within the Australian Agricultural sector.</p>
<div class="divider abs"></div>

<article class="card abs" style="left:130px">
  <div class="photo" role="img" aria-label="Combine harvester in a wheat field" style="background:linear-gradient(180deg,#8fb0c8 0%,#c9c0a0 40%,#e0b640 60%,#c99520 100%)"></div>
  <h3>Our Mission:</h3>
  <p>We are here to provide solutions to ALL of our<br>Clients needs and desires within the Agricultural</p>
</article>
<article class="card abs" style="left:329px">
  <div class="photo" role="img" aria-label="Farmer standing in front of a red tractor" style="background:linear-gradient(180deg,#5e7a3c 0%,#8a4a3a 45%,#6d9a3a 100%)"></div>
  <h3>Our Team:</h3>
  <p>Our team has worked with some of the largest &amp;<br>oldest Agricultural companies in</p>
</article>
<article class="card abs" style="left:526px">
  <div class="photo" role="img" aria-label="Black angus cattle grazing on green pasture" style="background:linear-gradient(180deg,#4a5a3a 0%,#2a2a26 45%,#5f9a34 80%,#7ab040 100%)"></div>
  <h3>Services Approach:</h3>
  <p>MHP offers a tailored service in order to meet the<br>objectives and outcomes for each and every client.</p>
</article>

<section class="band abs" role="img" aria-label="Flock of sheep on pasture tinted green">
  <div class="band-text abs">
    <p>We are a strategic advisory, investment manager and<br>problem solver with the Australian Agricultural sector.</p>
    <p>We are here to provide solutions to ALL of our Clients<br>needs and desires within the Agricultural space.</p>
  </div>
</section>

<div class="video abs" role="img" aria-label="Video still of a combine harvester in a wheat field">
  <svg class="play abs" viewBox="0 0 34 24" width="34" height="24" aria-hidden="true"><rect width="34" height="24" rx="5" fill="#222"/><path d="M13 6 L23 12 L13 18 Z" fill="#fff"/></svg>
</div>
<section class="services abs">
  <h2>Some of our services include:</h2>
  <p class="lead">Tailored advisory across grain, livestock and supply chains for growers, investors and food businesses. We deliver clear, practical outcomes.</p>
  <ul>
    <li>Food Security / Supply</li>
    <li>Procurement strategies within and across agricultural supplychains</li>
    <li>Strategic Agribusiness advice for both Australian and Chinese based agricultural enterprises</li>
    <li>M&amp;A / Due Diligence</li>
    <li>Corporate governance &amp; risk management strategies.</li>
  </ul>
</section>

<footer class="site-footer abs">
  <div class="signup abs f-title">Sign up to receive email updates</div>
  <div class="signup-form abs"><div class="field">Enter Email Address:</div><div class="btn">Subscribe</div></div>
  <div class="contact abs">
    <div class="f-title">Contact Us</div>
    <div class="addr">Field Lane 412, Brookvale<br>306 , Harvest Road</div>
    <div class="phone">(02) 5550 1846</div>
  </div>
  <svg class="social abs" width="110" height="26" viewBox="0 0 110 26" aria-label="Social links">
    <g fill="none" stroke="#ddd" stroke-width="1.2">
      <circle cx="12" cy="13" r="11"/><circle cx="41" cy="13" r="11"/><circle cx="69" cy="13" r="11"/><circle cx="96" cy="13" r="11"/>
    </g>
  </svg>
  <div class="copyright abs">Copyright © 2015 All Rights Reserved.</div>
</footer>

</body>
</html>
```